Create a fantasy eBook cover for a Catholic Novel

I wrote a novel called Blue Lantern Harvest, The central event occurs when a priest drops a communion wafer on a lady's red sneaker.
I need the the image to show a communion wafer on top of the sneaker.
The sneaker is magical in that it is flashing so any effect you can apply that would communicate that electric activity emanating from the sneaker would be helpful.

The complete book title is:

Blue Lantern Harvest
by Daniel Oberlitz

Ideal dimensions for cover files are 2,560 pixels in height x 1,600 pixels in width. image should be 2500 pixels in height. Minimum dimensions of 1000 pixels in height and 625 pixels in width.

```html
<!DOCTYPE html>
<html lang="en">
<head>
<meta charset="utf-8">
<title>Blue Lantern Harvest — Daniel Oberlitz</title>
<link rel="stylesheet" href="https://fonts.googleapis.com/css2?family=Bebas+Neue&family=Montserrat:wght@800&display=swap">
<style>
  :root {
    --night: #08122e;
    --deep-blue: #0f2a8c;
    --electric-blue: #3a5fe0;
    --burst-white: #eef1ff;
    --title-white: #ffffff;
    --title-shadow: #050a1c;
    --sneaker-red: #b8241c;
    --sneaker-dark: #6e1410;
  }
  html, body {
    margin: 0;
    padding: 0;
    width: 750px;
    height: 1200px;
    overflow: hidden;
    background: var(--night);
  }
  .cover {
    position: relative;
    width: 750px;
    height: 1200px;
    overflow: hidden;
    background:
      radial-gradient(ellipse 260px 340px at 375px 640px, var(--burst-white) 0%, rgba(200,210,255,0.85) 22%, rgba(90,120,235,0.6) 48%, rgba(20,50,170,0) 80%),
      radial-gradient(ellipse 520px 620px at 375px 620px, var(--electric-blue) 0%, var(--deep-blue) 55%, var(--night) 100%);
  }
  .burst {
    position: absolute;
    inset: 0;
  }
  .title {
    position: absolute;
    top: 58px;
    left: 0;
    width: 750px;
    margin: 0;
    text-align: center;
    font-family: "Bebas Neue", "Oswald", sans-serif;
    font-weight: 400;
    font-size: 140px;
    line-height: 137px;
    letter-spacing: 0.16em;
    color: var(--title-white);
    text-shadow: 7px 5px 0 var(--title-shadow);
  }
  .title span {
    display: block;
    margin-right: -0.16em;
  }
  .title .word-long {
    font-size: 128px;
    letter-spacing: 0.12em;
    margin-right: -0.12em;
  }
  .artwork {
    position: absolute;
    left: 88px;
    top: 560px;
    width: 610px;
    height: 530px;
  }
  .author {
    position: absolute;
    left: 0;
    top: 1110px;
    width: 750px;
    margin: 0;
    text-align: center;
    font-family: "Montserrat", sans-serif;
    font-weight: 800;
    font-size: 34px;
    letter-spacing: 0.42em;
    color: var(--title-white);
  }
  .author span {
    margin-right: -0.42em;
  }
</style>
</head>
<body>
  <main class="cover">
    <svg class="burst" width="750" height="1200" viewBox="0 0 750 1200" aria-hidden="true">
      <defs>
        <radialGradient id="glow" cx="375" cy="620" r="420" gradientUnits="userSpaceOnUse">
          <stop offset="0" stop-color="#ffffff" stop-opacity="0.55"/>
          <stop offset="0.5" stop-color="#9fb2ff" stop-opacity="0.18"/>
          <stop offset="1" stop-color="#1a2f9a" stop-opacity="0"/>
        </radialGradient>
      </defs>
      <g fill="url(#glow)">
        <polygon points="375,620 0,560 0,600"/>
        <polygon points="375,620 0,700 0,760"/>
        <polygon points="375,620 750,560 750,610"/>
        <polygon points="375,620 750,700 750,770"/>
        <polygon points="375,620 340,1200 410,1200"/>
        <polygon points="375,620 200,1200 250,1200"/>
        <polygon points="375,620 520,1200 570,1200"/>
        <polygon points="375,620 350,200 400,200"/>
        <polygon points="375,620 120,260 160,240"/>
        <polygon points="375,620 620,250 660,270"/>
      </g>
    </svg>

    <h1 class="title">
      <span>Blue</span>
      <span class="word-long">Lantern</span>
      <span>Harvest</span>
    </h1>

    <svg class="artwork" width="610" height="530" viewBox="0 0 610 530" role="img" aria-label="Photograph of a red high-top canvas sneaker with loose laces, a round white communion wafer marked with a cross resting beside it">
      <defs>
        <radialGradient id="sneaker-tone" cx="0.45" cy="0.5" r="0.6">
          <stop offset="0" stop-color="var(--sneaker-red)"/>
          <stop offset="0.7" stop-color="var(--sneaker-dark)" stop-opacity="0.85"/>
          <stop offset="1" stop-color="var(--sneaker-dark)" stop-opacity="0"/>
        </radialGradient>
      </defs>
      <ellipse cx="300" cy="280" rx="300" ry="250" fill="url(#sneaker-tone)"/>
    </svg>

    <p class="author"><span>Daniel Oberlitz</span></p>
  </main>
</body>
</html>
```